A r&b and house DJ needs a new Graphically pleasing and trendy website for fans and potential client

Want a new design for a dj website. This website wont be updated often so needs to look very graphically pleasing and just be a point of call where fans and potential clients can come and see information about the dj etc.

Needs to have short bio , social network links, and a enquiry button.

You can use some stock images for the moment as some professional images are going to be taken.

Others DJ websites:

https://www.djvornley.com/
http://www.pelkansoutar.com/
http://vomaro.com/
http://uletto.com/
http://www.dorianwelkby.co.uk/gb/home
http://www.fumbrelquix.com/
http://plinvaro.nl/

LOGO LINK IS HERE

https://www.filecrate-example.com/s/kq7wz2m9tnh4xa1/DJ_Vellum_logo.eps?dl=0

Target Market(s)

Fans and also prospective clients ( Nightclubs, Record Labels)

Industry/Entity Type

House

Font styles to use
Sans Serif

Requirements
Must have
• Small Bio, Social Network Links, Enquiry Button.
Nice to have
• Social network links

```html
<!DOCTYPE html>
<html lang="en">
<head>
<meta charset="utf-8">
<title>Vellum Sound Co</title>
<link href="https://fonts.googleapis.com/css2?family=Arvo:wght@400;700&family=Lato:ital,wght@0,400;0,700;1,400&display=swap" rel="stylesheet">
<style>
:root{
  --orange:#f26a2a;
  --ink:#333333;
  --white:#ffffff;
  --bio-bg:#e4e7f3;
  --dark:#2d2d2d;
  --darker:#262626;
  --blue:#3d54b0;
  --blue-deep:#31449a;
  --muted:#cfcfcf;
}
*{margin:0;padding:0;box-sizing:border-box}
html,body{width:829px;height:1200px;overflow:hidden}
body{position:relative;font-family:'Lato',sans-serif;color:var(--ink);background:var(--white)}
.abs{position:absolute}

/* header */
.site-header{left:0;top:0;width:829px;height:71px;background:var(--white)}
.brand{left:90px;top:11px;font-family:'Arvo',serif;color:var(--ink);font-size:20px;line-height:24px}
.nav{top:28px;left:346px;display:flex;align-items:center;font-family:'Arvo',serif;font-size:9.5px;letter-spacing:.3px;color:var(--ink)}
.nav .active{border:1.5px solid var(--orange);color:var(--orange);width:60px;height:25px;display:flex;align-items:center;justify-content:center;margin-right:22px}
.nav .item{display:flex;align-items:center}
.nav .sep{margin:0 12px;color:var(--ink)}

/* hero */
.hero{left:0;top:71px;width:829px;height:406px;background:radial-gradient(ellipse at 70% 45%,#c8561f 0%,#7a3312 30%,#3a3a12 55%,#1b1e0b 80%)}
.hero-arrow{width:28px;height:28px;border-radius:50%;background:var(--white);display:flex;align-items:center;justify-content:center;top:197px}
.player{position:absolute;left:90px;top:335px;width:649px;height:54px;display:flex}
.player .label{width:135px;background:var(--blue-deep);color:#c9d3ff;font-family:'Arvo',serif;font-size:11.5px;display:flex;align-items:center;justify-content:center}
.player .track{width:433px;background:var(--blue);position:relative}
.player .title{position:absolute;left:56px;top:14px;color:var(--white);font-family:'Arvo',serif;font-size:9px}
.player .share{position:absolute;right:19px;top:16px;color:var(--white);font-size:8px;font-weight:700}
.player .bar{position:absolute;left:56px;top:36px;width:359px;height:3px;background:#e3e6f3}
.player .bar span{display:block;width:14px;height:3px;background:var(--orange)}
.player .social{width:81px;background:var(--blue);border-left:1px solid #2b3c88;display:flex;align-items:center;justify-content:space-around;color:#1d2a66;font-size:8px;font-weight:700}

/* bio */
.bio{left:0;top:477px;width:829px;height:237px;background:var(--bio-bg);text-align:center}
.bio h2{position:absolute;left:0;width:829px;top:50px;font-family:'Arvo',serif;font-weight:400;font-size:25px}
.bio .lead{position:absolute;left:0;width:829px;top:92px;color:var(--orange);font-family:'Arvo',serif;font-size:10px}
.bio p{position:absolute;left:90px;width:649px;top:114px;font-size:9px;line-height:16.6px;color:#444}
.btn{background:var(--orange);color:var(--white);font-size:9px;display:flex;align-items:center;justify-content:center}
.bio .btn{position:absolute;left:370px;top:175px;width:90px;height:25px}

/* media */
.media{left:0;top:714px;width:829px;height:394px;background:var(--dark);color:var(--muted)}
.section-title{font-family:'Arvo',serif;font-size:13px;color:var(--white)}
.section-title em{font-style:normal;color:var(--orange)}
.video-thumb{width:206px;height:115px;border:3px solid #555;display:flex;align-items:center;justify-content:center}
.video-thumb .play{width:28px;height:28px;border-radius:50%;border:2px solid var(--white);background:rgba(0,0,0,.35);display:flex;align-items:center;justify-content:center}
.video-text{width:195px}
.video-text h3{font-family:'Arvo',serif;font-weight:400;font-size:11px;color:var(--orange);margin-bottom:13px}
.video-text p{font-size:8.8px;line-height:14px;text-align:justify}
.video-text .more{font-family:'Arvo',serif;font-size:8.5px;color:var(--orange);margin-top:11px}
.post-card{width:202px;height:68px;background:var(--white);color:#555;font-size:8.6px;line-height:16.5px;padding:11px 12px;text-align:justify}
.post-card::after{content:"";position:absolute;left:20px;bottom:-7px;border-left:7px solid transparent;border-right:7px solid transparent;border-top:7px solid var(--white)}
.avatar{width:40px;height:40px;border-radius:50%;border:2px solid var(--white)}
.post-meta{font-size:8px;font-style:italic;color:#ddd}

/* footer */
.site-footer{left:0;top:1108px;width:829px;height:92px;background:var(--darker)}
.social-links{left:92px;top:22px;display:flex;gap:12px}
.social-links span{font-size:8px;color:#9fb0e6;display:flex;align-items:center;gap:4px}
.social-links i{display:inline-block;width:9px;height:9px;border-radius:50%;background:#3f5fc2}
.copyright{left:91px;top:56px;font-size:9px;color:#aaa;letter-spacing:.2px}
.copyright span{color:var(--orange)}
.site-footer .btn{position:absolute;left:593px;top:34px;width:145px;height:29px;font-size:9.5px}
</style>
</head>
<body>

<header class="abs site-header">
  <div class="abs brand">VELLUM<br>SOUND CO</div>
  <nav class="abs nav">
    <span class="active">HOME</span>
    <span class="item">BIOGRAPHY<span class="sep">|</span>GALLERY<span class="sep">|</span>VIDEOS<span class="sep">|</span>MIXES<span class="sep">|</span>CONTACT</span>
  </nav>
</header>

<section class="abs hero" role="img" aria-label="DJ in an orange shirt wearing headphones behind decks, crowd lights in background">
  <div class="abs hero-arrow" style="left:75px"><svg width="10" height="12" viewBox="0 0 10 12"><path d="M7 1 2 6l5 5" fill="none" stroke="#333" stroke-width="2.4"/></svg></div>
  <div class="abs hero-arrow" style="left:727px"><svg width="10" height="12" viewBox="0 0 10 12"><path d="M3 1l5 5-5 5" fill="none" stroke="#333" stroke-width="2.4"/></svg></div>
  <div class="player">
    <div class="label">LATEST MUSIC</div>
    <div class="track">
      <svg class="abs" style="left:14px;top:14px" width="26" height="26" viewBox="0 0 26 26"><circle cx="13" cy="13" r="11.5" fill="none" stroke="#1d2a66" stroke-width="2"/><path d="M10 8v10l8-5z" fill="#1d2a66"/></svg>
      <div class="title">EXOTIC ON AIR - ALBUM 02</div>
      <div class="share">SHARE IT</div>
      <div class="bar"><span></span></div>
    </div>
    <div class="social"><span>Friendly</span><span>Chirply</span></div>
  </div>
</section>

<section class="abs bio">
  <h2>BIO</h2>
  <div class="lead">NEQUE PORRO QUISQUAM EST QUI DOLOREM IPSUM QUIA DOLOR SIT..</div>
  <p>Lorem ipsum dolor sit amet, consectetur adipiscing elit, sed do eiusmod tempor incididunt ut labore et dolore magna aliqua. Ut enim ad minim veniam, quis nostrud exercitation ullamco laboris nisi ut aliquip ex ea commodo consequat. Duis aute irure dolor in reprehenderit in voluptate velit esse cillum dolore eu fugiat nulla pariatur. Excepteur sint occaecat cupidatat non proident</p>
  <div class="btn">READ MORE</div>
</section>

<section class="abs media">
  <div class="abs section-title" style="left:89px;top:57px">VIEW OUR LATEST <em>VIDEO'S</em></div>
  <div class="abs section-title" style="left:537px;top:57px"><em>BLOG</em> POST</div>

  <div class="abs video-thumb" style="left:88px;top:84px;background:linear-gradient(90deg,#8a8a86 0%,#6b6250 45%,#c99a18 75%,#d6a91c 100%)" role="img" aria-label="Hand on a turntable with yellow background">
    <span class="play"><svg width="10" height="12" viewBox="0 0 10 12"><path d="M1 0v12l9-6z" fill="#fff"/></svg></span>
  </div>
  <div class="abs video-text" style="left:310px;top:87px">
    <h3>Nemo Enim Ipsam Voluptatem</h3>
    <p>Sed ut perspiciatis unde omnis iste natus error sit voluptatem accusantium doloremque lau dantium, totam rem aperiam, eaque ipsa quae ab illo inventore veritatis et.</p>
    <div class="more">[ View More ]</div>
  </div>

  <div class="abs video-thumb" style="left:88px;top:225px;background:linear-gradient(100deg,#5a2a22 0%,#8a3a2c 35%,#3a3330 60%,#a45a1e 100%)" role="img" aria-label="Hands adjusting a mixing desk">
    <span class="play"><svg width="10" height="12" viewBox="0 0 10 12"><path d="M1 0v12l9-6z" fill="#fff"/></svg></span>
  </div>
  <div class="abs video-text" style="left:310px;top:229px">
    <h3>Nemo Enim Ipsam Voluptatem</h3>
    <p>Sed ut perspiciatis unde omnis iste natus error sit voluptatem accusantium doloremque lau dan tium, totam rem aperiam, eaque ipsa quae ab illo inventore veritatis et.</p>
    <div class="more">[ View More ]</div>
  </div>

  <div class="abs post-card" style="left:537px;top:88px">Lorem ipsum dolor sit amet, consectetur adipiscing elit, sed do eiusmod tempor incididunt ut labore et dolore</div>
  <div class="abs avatar" style="left:541px;top:172px;background:linear-gradient(#c9a58a,#8d6a55)" role="img" aria-label="Author portrait"></div>
  <div class="abs post-meta" style="left:593px;top:187px">by Tom Welbury &nbsp; | &nbsp;2 hrs. ago</div>

  <div class="abs post-card" style="left:537px;top:241px">Lorem ipsum dolor sit amet, consectetur adipiscing elit, sed do eiusmod tempor incididunt ut labore et dolore</div>
  <div class="abs avatar" style="left:541px;top:325px;background:linear-gradient(#e3c9a0,#b08a6a)" role="img" aria-label="Author portrait"></div>
  <div class="abs post-meta" style="left:593px;top:340px">by Tom Welbury &nbsp; | &nbsp;2 hrs. ago</div>
</section>

<footer class="abs site-footer">
  <div class="abs social-links">
    <span><i></i>Friendly</span>
    <span><i></i>Chirply</span>
    <span><i></i>Clipstream</span>
  </div>
  <div class="abs copyright">Copyright © &nbsp;2015. <span>Vellum Sound Co</span> All Right Reserved</div>
  <div class="btn">GET AN ENQUIRY NOW</div>
</footer>

</body>
</html>
```